Lantern Hill Publicity is a new boutique Press Office with a small roster of well-chosen clients across an array of disciplines; from Art and Technology to Restaurants and Fashion. Based in Greenpoint Brooklyn, Lantern Hill Publicity achieves outstanding results through hard work, tenacity, efficiency and a sense of humor. We need a simple, versatile and classic design. We would like each side of the card to be white text on a black background.

Boutique

```html
<!DOCTYPE html>
<html lang="en">
<head>
<meta charset="utf-8">
<title>Lantern Hill Publicity — Business Card</title>
<link rel="stylesheet" href="https://fonts.googleapis.com/css2?family=Libre+Baskerville:wght@400&family=PT+Sans:wght@400&display=swap">
<style>
  :root {
    --stage: #4d4d4d;
    --card: #000000;
    --ink: #ffffff;
    --shadow: rgba(0, 0, 0, 0.45);
  }
  * { margin: 0; padding: 0; box-sizing: border-box; }
  html, body {
    width: 1200px;
    height: 1200px;
    overflow: hidden;
    background: var(--stage);
  }
  .stage {
    position: relative;
    width: 1200px;
    height: 1200px;
    background: var(--stage);
  }
  .card {
    position: absolute;
    left: 258px;
    width: 686px;
    height: 389px;
    background: var(--card);
    color: var(--ink);
    box-shadow: 0 6px 18px var(--shadow);
  }
  .card--front { top: 187px; }
  .card--back { top: 624px; }

  .wordmark {
    position: absolute;
    font-family: "Libre Baskerville", serif;
    font-weight: 400;
    font-size: 24px;
    line-height: 1.35;
    letter-spacing: 0.14em;
    text-transform: uppercase;
    text-align: center;
    color: var(--ink);
    white-space: nowrap;
    transform: translate(-50%, -50%);
  }
  .card--front .wordmark { left: 50%; top: 52%; }
  .card--back .wordmark { left: 74%; top: 33%; }

  .contact {
    position: absolute;
    left: 51px;
    top: 222px;
  }
  .contact__name {
    font-family: "Libre Baskerville", serif;
    font-size: 23px;
    font-weight: 400;
    margin-bottom: 20px;
  }
  .contact__list { list-style: none; }
  .contact__item {
    display: flex;
    align-items: center;
    gap: 8px;
    font-family: "PT Sans", sans-serif;
    font-size: 16px;
    line-height: 23px;
  }
  .contact__icon {
    width: 12px;
    height: 12px;
    fill: var(--ink);
    stroke: var(--ink);
  }
</style>
</head>
<body>
<main class="stage">
  <section class="card card--front" aria-label="Card front">
    <p class="wordmark">Lantern Hill<br>Publicity</p>
  </section>

  <section class="card card--back" aria-label="Card back">
    <p class="wordmark">Lantern Hill<br>Publicity</p>
    <div class="contact">
      <h1 class="contact__name">Mara Ellison</h1>
      <ul class="contact__list">
        <li class="contact__item">
          <svg class="contact__icon" viewBox="0 0 12 12" aria-hidden="true">
            <path stroke="none" d="M1 4 Q6 0 11 4 L9.5 5 L8 3.8 L4 3.8 L2.5 5 Z"/>
            <rect stroke="none" x="2" y="6" width="8" height="5" rx="1"/>
          </svg>
          (00) 000-0000
        </li>
        <li class="contact__item">
          <svg class="contact__icon" viewBox="0 0 12 12" aria-hidden="true">
            <rect stroke="none" x="0.5" y="2.5" width="11" height="7.5"/>
            <path fill="none" stroke="#000" stroke-width="1" d="M0.5 2.5 L6 7 L11.5 2.5"/>
          </svg>
          mellison@lanternhillpr.com
        </li>
        <li class="contact__item">
          <svg class="contact__icon" viewBox="0 0 12 12" aria-hidden="true" fill="none" stroke-width="0.9">
            <circle cx="6" cy="6" r="5"/>
            <ellipse cx="6" cy="6" rx="2.2" ry="5"/>
            <path d="M1 6 H11 M2 3.5 H10 M2 8.5 H10"/>
          </svg>
          www.lanternhillpr.com
        </li>
      </ul>
    </div>
  </section>
</main>
</body>
</html>
```